BrambleWorks business card

Looking for business card design that supports our company/software values. We have 2 logo designs at the moment but open to change if you think you can enhance the brand. Check out website www.brambleworks.com.au.

Target Market(s)

Education

Contact Information for Business Card

Name, title, mobile, email and website

Font styles to use
Sans Serif

Colors

Designer to choose colors to be used in the design.

Requirements
Must have
• BrambleWorks logo with tree and tagline on rear side with dark grey background colour

```html
<!DOCTYPE html>
<html lang="en">
<head>
<meta charset="utf-8">
<title>BrambleWorks business card</title>
<link rel="stylesheet" href="https://fonts.googleapis.com/css2?family=Ubuntu:wght@400&family=Crimson+Text:wght@400&display=swap">
<style>
  :root {
    --canvas: #dadbda;
    --card-front: #fefefe;
    --card-back: #8a8a8a;
    --ink-dark: #4a4a4a;
    --ink-title: #2e2e2e;
    --ink-light: #ffffff;
  }
  html, body {
    margin: 0;
    padding: 0;
    width: 1200px;
    height: 1200px;
    overflow: hidden;
    background: var(--canvas);
  }
  .card {
    position: absolute;
    top: 400px;
    left: 240px;
    width: 720px;
    height: 400px;
    display: flex;
  }
  .card-front {
    position: relative;
    width: 327px;
    height: 100%;
    background: var(--card-front);
    overflow: hidden;
  }
  .brand-dot {
    position: absolute;
    left: 52px;
    top: 175px;
    width: 52px;
    height: 52px;
    border-radius: 50%;
    background: var(--ink-dark);
  }
  .brand {
    position: absolute;
    left: 139px;
    top: 175px;
    width: 152px;
    font-family: "Ubuntu", sans-serif;
    color: var(--ink-dark);
  }
  .brand-name {
    font-size: 23px;
    line-height: 1;
    white-space: nowrap;
    padding-bottom: 5px;
    border-bottom: 1px solid var(--ink-dark);
  }
  .brand-tagline {
    font-size: 11.5px;
    margin-top: 4px;
    padding-left: 2px;
    letter-spacing: 0.3px;
    white-space: nowrap;
  }
  .card-back {
    position: relative;
    width: 393px;
    height: 100%;
    background: var(--card-back);
    font-family: "Crimson Text", serif;
    text-align: center;
    color: var(--ink-light);
  }
  .holder-name {
    position: absolute;
    left: 0;
    right: 0;
    top: 151px;
    margin: 0;
    font-size: 37px;
    font-weight: 400;
    line-height: 1;
    padding-left: 14px;
  }
  .holder-title {
    position: absolute;
    left: 0;
    right: 0;
    top: 192px;
    margin: 0;
    font-size: 30px;
    line-height: 1;
    color: var(--ink-title);
    padding-left: 14px;
  }
  .contact-list {
    position: absolute;
    left: 0;
    right: 0;
    top: 246px;
    margin: 0;
    padding: 0 0 0 26px;
    list-style: none;
    font-size: 19px;
    line-height: 26.5px;
  }
</style>
</head>
<body>
  <div class="card">
    <section class="card-front">
      <div class="brand-dot"></div>
      <div class="brand">
        <div class="brand-name">BrambleWorks</div>
        <div class="brand-tagline">Student Success Platform</div>
      </div>
    </section>
    <section class="card-back">
      <h1 class="holder-name">Alex Harlow</h1>
      <p class="holder-title">title</p>
      <ul class="contact-list">
        <li>0400 555 218 764</li>
        <li>contact@brambleworks.com.au</li>
        <li>www.brambleworks.com.au</li>
      </ul>
    </section>
  </div>
</body>
</html>
```